【依頼目的/概要】
近日中に出版する予定の電子書籍(kindle版)の表紙デザインをお願いします。

【画像サイズ】
表紙ファイルの理想的な寸法は2560x1600ピクセルです。
注:画像の寸法は1000x625ピクセル以上であることが必要です。
画像の最大寸法は10000x10000ピクセルです。

【タイトル】
夜明けの庭で見つけた静かな暮らしの小さな習慣

【著者】
医師(循環器専門医、瑞穂橋文化振興会公認スポーツドクター)
桐原晴臣

【本の内容】
医師である私自身の実践したダイエット法について説明した本です。
ただ「食べるのガマンして体重が減りました」だけでは脂肪だけではなく、筋肉まで落ちてしまいます。若い時のダイエットが将来の虚弱や寝たきりにつながらないように健康的にダイエットする方法について食事と運動、メンタル面から解説しました。

*本文を参考資料として添付します。

【デザイン要望】
特にイメージはありませんので自由な発想でのデザインご応募楽しみにしています

*その他、必要な情報がありましたらお問い合わせください。

どの性別、どの年齢の人にも手に取ってもらいやすく、内容に関しても一見してわかりやすいデザインだと感じました。

どのデザインも甲乙つけがたく、大変悩みました。多数の方にご応募いただき、誠にありがとうございました。皆様とまたご縁がありましたらよろしくお願いいたします。今回は大変ありがとうございました。

```html
<!DOCTYPE html>
<html lang="ja">
<head>
<meta charset="utf-8">
<title>夜明けの庭で見つけた静かな暮らしの小さな習慣</title>
<link href="https://fonts.googleapis.com/css2?family=Dela+Gothic+One&family=Noto+Sans+JP:wght@500;700;900&display=swap" rel="stylesheet">
<style>
  :root {
    --paper: #ffffff;
    --ink: #111111;
    --red: #d3121b;
    --yellow: #f6d21a;
    --gold-light: #f7e7a6;
    --gold-mid: #e7c463;
    --gold-deep: #c99a2e;
    --shade-dark: #3a3a3a;
  }
  * { margin: 0; padding: 0; box-sizing: border-box; }
  html, body { width: 750px; height: 1200px; overflow: hidden; background: var(--paper); }
  .cover {
    position: relative; width: 750px; height: 1200px; overflow: hidden;
    background: var(--paper);
    font-family: "Noto Sans JP", sans-serif; color: var(--ink);
  }
  .figure-art {
    position: absolute; left: 0; top: 0; width: 750px; height: 880px;
    background:
      radial-gradient(ellipse 38% 30% at 20% 32%, var(--shade-dark) 0%, rgba(58,58,58,0.55) 45%, rgba(255,255,255,0) 75%),
      radial-gradient(ellipse 38% 30% at 80% 32%, var(--shade-dark) 0%, rgba(58,58,58,0.55) 45%, rgba(255,255,255,0) 75%),
      radial-gradient(ellipse 50% 20% at 50% 8%, #555 0%, rgba(85,85,85,0) 80%),
      radial-gradient(ellipse 45% 40% at 50% 80%, #bdbdbd 0%, rgba(255,255,255,0) 80%),
      var(--paper);
  }
  .title-top, .title-main, .title-mid, .title-bottom {
    position: absolute; left: 0; right: 0; text-align: center;
    font-family: "Dela Gothic One", sans-serif; line-height: 1; white-space: nowrap;
    paint-order: stroke fill;
  }
  .title-top { top: 200px; color: var(--red); -webkit-text-stroke: 10px var(--paper); }
  .title-top .lead { font-size: 62px; }
  .title-top .sub { font-size: 46px; }
  .title-top .accent {
    display: inline-block; font-size: 24px; color: var(--ink);
    background: var(--yellow); -webkit-text-stroke: 0;
    padding: 8px 8px; margin: 0 6px; vertical-align: 12px;
    border-radius: 50%;
  }
  .title-main {
    top: 300px; font-size: 210px; letter-spacing: 4px;
    color: var(--yellow); -webkit-text-stroke: 12px var(--paper);
  }
  .title-mid {
    top: 550px; font-size: 62px; color: var(--red);
    -webkit-text-stroke: 12px var(--paper);
  }
  .title-mid .particle { font-size: 46px; }
  .title-bottom {
    top: 632px; font-size: 100px; color: var(--red);
    -webkit-text-stroke: 12px var(--paper);
  }
  .author {
    position: absolute; right: 26px; top: 752px; text-align: right; line-height: 1.3;
  }
  .author .role { font-size: 18px; font-weight: 700; }
  .author .name { font-size: 44px; font-weight: 900; letter-spacing: 3px; margin-top: 2px; }
  .band {
    position: absolute; left: 0; top: 866px; width: 750px; height: 334px;
    background: linear-gradient(115deg, var(--gold-light) 0%, var(--gold-mid) 40%, var(--gold-deep) 75%, var(--gold-mid) 100%);
  }
  .band-reveal {
    position: absolute; left: 14px; top: 880px; height: 310px;
    writing-mode: vertical-rl; white-space: nowrap;
    font-family: "Dela Gothic One", sans-serif;
    font-size: 98px; line-height: 1; color: var(--red);
  }
  .band-label {
    position: absolute; left: 132px; top: 882px; height: 310px;
    writing-mode: vertical-rl; white-space: nowrap;
    font-family: "Dela Gothic One", sans-serif;
    font-size: 58px; line-height: 1.2; color: var(--paper);
    -webkit-text-stroke: 8px var(--ink); paint-order: stroke fill;
  }
  .band-copy {
    position: absolute; right: 20px; top: 884px; height: 306px;
    writing-mode: vertical-rl; white-space: nowrap; font-weight: 700; color: var(--ink);
  }
  .band-copy .headline { font-size: 40px; font-weight: 900; line-height: 1.15; }
  .band-copy .body { font-size: 24px; line-height: 1.2; margin-right: 8px; }
</style>
</head>
<body>
  <main class="cover">
    <div class="figure-art" role="img" aria-label="力こぶを見せる筋肉質な上半身のモノクロ写真"></div>

    <h1 class="title">
      <span class="title-top"><span class="lead">夜明けの庭で</span><span class="accent">そっと</span><span class="sub">見つけた</span></span>
      <span class="title-main">静かな</span>
      <span class="title-mid">暮らし<span class="particle">の</span></span>
      <span class="title-bottom">小さな習慣</span>
    </h1>

    <div class="author">
      <p class="role">循環器専門医</p>
      <p class="role">瑞穂橋文化振興会公認スポーツドクター</p>
      <p class="name">桐原晴臣</p>
    </div>

    <section class="band"></section>
    <p class="band-reveal">大公開</p>
    <p class="band-label">ドクターズ<br>ダイエット</p>
    <p class="band-copy">
      <span class="headline">痩せるだけが<br>ゴールじゃない</span><br>
      <span class="body">リバウンドこそが<br>ダイエットのチャンス!?<br>モチベーションを維持<br>できるのは不純な動機!?<br>科学的・効率的な実践法で<br>健康的かつ、思い通りに<br>反応する身体に変える!!</span>
    </p>
  </main>
</body>
</html>
```